Envelope Design Project

I will need two envelopes to be designed:-

DL size
C4 size

Please see uploaded documents for Design specs:

1) Design specs provided by printer (doc called DL Envelope Specs)
2) Design specs to comply with Kestrel Mailways requirements (doc called Kestrel Mailways Envelope Design Requirements)

Please adhere to the above for final design. Many thanks.

Target Market(s)

Real Estate Agents, Strata Managers, Builders, Architects, Business Owners

Industry/Entity Type

Printer

Requirements
Must have
• In top left corner
- Logo
- Return address - Suite 5, 19 Wattlebark Rd, Marrowick, NSW 2417

```html
<!DOCTYPE html>
<html lang="en">
<head>
<meta charset="utf-8">
<title>Norhaven Hazard &amp; Safety – Envelope Set</title>
<link href="https://fonts.googleapis.com/css2?family=Questrial&display=swap" rel="stylesheet">
<style>
  :root {
    --stage: #e4e5e6;
    --paper: #ffffff;
    --edge: #c9cacc;
    --charcoal: #3a3b3d;
    --lime: #9dc93b;
    --ink: #4a4b4d;
  }
  * { margin: 0; padding: 0; box-sizing: border-box; }
  html, body { width: 1200px; height: 900px; overflow: hidden; }
  body {
    position: relative;
    background: var(--stage);
    font-family: "Questrial", "Century Gothic", sans-serif;
    color: var(--ink);
  }
  .envelope {
    position: absolute;
    background: var(--paper);
    border: 1px solid var(--edge);
    box-shadow: 0 2px 6px rgba(0,0,0,0.12);
  }
  .dl-back  { left: 152px; top: 85px;  width: 399px; height: 208px; }
  .dl-front { left: 97px;  top: 167px; width: 398px; height: 199px; }
  .c4-back  { left: 503px; top: 342px; width: 588px; height: 418px; }
  .c4-front { left: 398px; top: 393px; width: 589px; height: 417px; }

  .flap-art { position: absolute; }
  .dl-back .flap-art {
    left: 0; top: 4px; width: 397px; height: 66px;
    border-radius: 0 0 20px 0;
    background: linear-gradient(90deg, var(--charcoal) 0%, #6f8a3a 45%, var(--lime) 100%);
  }
  .c4-back .flap-art {
    left: 517px; top: 4px; width: 69px; height: 410px;
    border-radius: 0 0 0 28px;
    background: linear-gradient(180deg, var(--charcoal) 0%, #6f8a3a 40%, var(--lime) 100%);
  }

  .tab { position: absolute; }
  .tab--charcoal { background: var(--charcoal); }
  .tab--lime { background: var(--lime); }

  .brand { position: absolute; display: flex; align-items: center; }
  .brand__square { background: var(--lime); flex: none; }
  .brand__name {
    color: var(--charcoal);
    font-weight: 400;
    line-height: 1.05;
    text-transform: uppercase;
  }
  .return-address {
    position: absolute;
    font-style: normal;
    color: var(--ink);
    line-height: 1.25;
  }

  /* DL front */
  .dl-front .tab--charcoal { left: 17px; width: 24px; height: 5px; }
  .dl-front .tab--lime { left: 46px; width: 40px; height: 5px; }
  .dl-front .tab--top { top: 0; }
  .dl-front .tab--bottom { bottom: 0; }
  .dl-front .brand { left: 17px; top: 16px; gap: 5px; }
  .dl-front .brand__square { width: 14px; height: 14px; }
  .dl-front .brand__name { font-size: 9px; }
  .dl-front .return-address { left: 19px; top: 172px; font-size: 6.5px; }

  /* C4 front */
  .c4-front .tab--charcoal { left: 26px; width: 34px; height: 6px; }
  .c4-front .tab--lime { left: 69px; width: 61px; height: 6px; }
  .c4-front .tab--top { top: 0; }
  .c4-front .tab--bottom { bottom: 0; height: 10px; }
  .c4-front .brand { left: 26px; top: 34px; gap: 8px; }
  .c4-front .brand__square { width: 26px; height: 26px; }
  .c4-front .brand__name { font-size: 15px; }
  .c4-front .return-address { left: 29px; top: 376px; font-size: 11px; }
</style>
</head>
<body>

  <div class="envelope dl-back">
    <div class="flap-art" role="img" aria-label="Flowing green and charcoal wave artwork along the top of the envelope back"></div>
  </div>

  <div class="envelope dl-front">
    <span class="tab tab--charcoal tab--top"></span>
    <span class="tab tab--lime tab--top"></span>
    <div class="brand">
      <span class="brand__square"></span>
      <span class="brand__name">Norhaven<br>Hazard &amp; Safety</span>
    </div>
    <address class="return-address">Suite 5, 19 Wattlebark Rd<br>Marrowick, NSW 2417</address>
    <span class="tab tab--charcoal tab--bottom"></span>
    <span class="tab tab--lime tab--bottom"></span>
  </div>

  <div class="envelope c4-back">
    <div class="flap-art" role="img" aria-label="Flowing green and charcoal wave artwork down the right edge of the envelope back"></div>
  </div>

  <div class="envelope c4-front">
    <span class="tab tab--charcoal tab--top"></span>
    <span class="tab tab--lime tab--top"></span>
    <div class="brand">
      <span class="brand__square"></span>
      <span class="brand__name">Norhaven<br>Hazard &amp; Safety</span>
    </div>
    <address class="return-address">Suite 5, 19 Wattlebark Rd<br>Marrowick, NSW 2417</address>
    <span class="tab tab--charcoal tab--bottom"></span>
    <span class="tab tab--lime tab--bottom"></span>
  </div>

</body>
</html>
```